Criação de Papelaria (6 itens) para Viagens & Lazer
" ATENDIMENTO PARA VIAGENS NACIONAIS E INTERNACIONAIS, RESERVAS DE HOTEIS E PACOTES DE VIAGENS, INDIVIDUAIS E GRUPOS "

```html
<!DOCTYPE html>
<html lang="pt-BR">
<head>
<meta charset="utf-8">
<title>VRN Tur – Pasta</title>
<link rel="stylesheet" href="https://fonts.googleapis.com/css2?family=Montserrat:wght@600;700;800&display=swap">
<style>
  :root {
    --royal: #1f3ed8;
    --royal-deep: #1530b8;
    --orange: #f5a01e;
    --paper: #f1f1f0;
    --ground: #e4e6ee;
    --ink: #ffffff;
  }
  * { margin: 0; padding: 0; box-sizing: border-box; }
  html, body { width: 1200px; height: 1200px; overflow: hidden; }
  body {
    background: var(--ground);
    font-family: "Montserrat", sans-serif;
    position: relative;
  }
  .folder-front, .folder-inside {
    position: absolute;
    top: 230px;
    width: 520px;
    height: 740px;
    box-shadow: 0 10px 30px rgba(20, 30, 80, .18);
  }
  .folder-front {
    left: 60px;
    background: var(--paper);
    border-top: 14px solid var(--orange);
  }
  .folder-front .bottom-band {
    position: absolute; left: 0; right: 0; bottom: 0;
    height: 12px; background: var(--orange);
  }
  .brand {
    position: absolute;
    top: 230px; left: 0; right: 0;
    display: flex; flex-direction: column; align-items: center;
  }
  .brand-row { display: flex; align-items: center; gap: 12px; }
  .brand-dot {
    width: 44px; height: 44px; border-radius: 50%;
    background: var(--royal);
  }
  .brand-name {
    font-weight: 800; font-size: 46px; color: var(--royal);
    letter-spacing: .5px;
  }
  .brand-tag {
    margin-top: 4px; margin-left: 56px;
    font-weight: 700; font-size: 13px; letter-spacing: 3px;
    color: var(--orange);
  }
  .folder-inside {
    left: 620px;
    background: var(--royal);
  }
  .map-area {
    position: absolute; left: 0; top: 0; width: 100%; height: 560px;
    background: linear-gradient(160deg, var(--paper) 0%, #e8e9ee 55%, var(--royal) 56%, var(--royal-deep) 100%);
  }
  .contact-strip {
    position: absolute; left: 40px; right: 40px; bottom: 70px;
    display: grid; grid-template-columns: 1fr 1fr; gap: 12px 24px;
  }
  .contact-item {
    display: flex; align-items: center; gap: 10px;
    font-weight: 600; font-size: 15px; color: var(--ink);
  }
  .contact-item svg { width: 20px; height: 20px; flex: none; }
  .folder-inside .bottom-band {
    position: absolute; left: 0; right: 0; bottom: 0;
    height: 14px; background: var(--orange);
  }
</style>
</head>
<body>
  <section class="folder-front">
    <div class="brand">
      <div class="brand-row">
        <span class="brand-dot"></span>
        <span class="brand-name">VRN Tur</span>
      </div>
      <span class="brand-tag">VIAGENS &amp; TURISMO</span>
    </div>
    <div class="bottom-band"></div>
  </section>

  <section class="folder-inside">
    <div class="map-area" role="img" aria-label="Mapa-múndi em linhas finas azuis sobre fundo claro"></div>
    <div class="contact-strip">
      <div class="contact-item">
        <svg viewBox="0 0 20 20"><circle cx="10" cy="10" r="10" fill="#f5a01e"/><path d="M7 5l2 2-1 1.5a6 6 0 0 0 3.5 3.5L13 11l2 2-1.5 1.5C9.5 14 6 10.5 5.5 6.5z" fill="#fff"/></svg>
        +55 (11) 3000-4120
      </div>
      <div class="contact-item">
        <svg viewBox="0 0 20 20"><circle cx="10" cy="10" r="10" fill="#f5a01e"/><rect x="5" y="6.5" width="10" height="7" rx="1" fill="#fff"/><path d="M5 7l5 3.5L15 7" stroke="#f5a01e" fill="none"/></svg>
        contato@vrntur.com.br
      </div>
      <div class="contact-item">
        <svg viewBox="0 0 20 20"><circle cx="10" cy="10" r="10" fill="#f5a01e"/><path d="M7 5l2 2-1 1.5a6 6 0 0 0 3.5 3.5L13 11l2 2-1.5 1.5C9.5 14 6 10.5 5.5 6.5z" fill="#fff"/></svg>
        +55 (11) 90000-5512
      </div>
      <div class="contact-item">
        <svg viewBox="0 0 20 20"><circle cx="10" cy="10" r="10" fill="#f5a01e"/><circle cx="10" cy="10" r="5" stroke="#fff" stroke-width="1.5" fill="none"/><path d="M5 10h10M10 5v10" stroke="#fff" stroke-width="1.2"/></svg>
        www.vrntur.com.br
      </div>
    </div>
    <div class="bottom-band"></div>
  </section>
</body>
</html>
```